IT Staffing and Application Development

We need a facebook page for our IT Technology and Staffing company based in North America called Pinecrest Solutions. We develop enterprise applications for respected fortune 500 companies. We also place top IT consultants to serve our clients needs. Please look at www.pinecrestsolutions-example.com for more details. The final design should communicate very high quality of our company, consultants and useful for marketing to new clients.
Updates

Target Market(s)

IT Directors, Managers, IT consultants, IT staffing

Industry/Entity Type

Marketing

Colors
acd036
3176b5
b768aa
f78f20

Requirements
Must have
• Please use the images and content in
www.pinecrestsolutions-example.com and should have all the content here
Nice to have
• Logo should indicated pinecrest capturing IT staffing, consulting and Application Development

```html
<!DOCTYPE html>
<html lang="en">
<head>
<meta charset="utf-8">
<title>Pinecrest Solutions – Facebook Cover</title>
<link href="https://fonts.googleapis.com/css2?family=Open+Sans:wght@300;400;700&display=swap" rel="stylesheet">
<style>
  :root {
    --green: #acd036;
    --blue: #3176b5;
    --purple: #b768aa;
    --orange: #f78f20;
    --photo-dark: #2f3a52;
    --photo-mid: #4c5872;
    --photo-light: #7a849a;
    --panel: rgba(40, 50, 72, 0.55);
    --headline: #8ec5ea;
    --white: #ffffff;
  }
  html, body {
    margin: 0;
    padding: 0;
    width: 1200px;
    height: 440px;
    overflow: hidden;
    background: var(--photo-dark);
  }
  .cover {
    position: relative;
    width: 1200px;
    height: 440px;
    overflow: hidden;
    font-family: "Open Sans", Arial, sans-serif;
    color: var(--white);
  }
  .cover__photo {
    position: absolute;
    inset: 0;
    background:
      radial-gradient(ellipse 420px 360px at 1020px 230px, rgba(150,158,178,0.55), transparent 70%),
      radial-gradient(ellipse 380px 260px at 520px 260px, rgba(110,120,145,0.45), transparent 75%),
      linear-gradient(90deg, var(--photo-dark) 0%, var(--photo-mid) 45%, var(--photo-light) 100%);
  }
  .brand-bar {
    position: absolute;
    top: 0; left: 0;
    width: 1200px;
    height: 10px;
    display: flex;
  }
  .brand-bar span { height: 100%; }
  .brand-bar .green  { width: 300px; background: var(--green); }
  .brand-bar .blue   { width: 304px; background: var(--blue); }
  .brand-bar .purple { width: 302px; background: var(--purple); }
  .brand-bar .orange { width: 294px; background: var(--orange); }

  .intro {
    position: absolute;
    top: 14px; left: 0;
    width: 440px;
    height: 112px;
    padding: 22px 0 0 17px;
    box-sizing: border-box;
    background: var(--panel);
  }
  .intro__headline {
    margin: 0;
    font-size: 19.5px;
    line-height: 22px;
    font-weight: 700;
    color: var(--headline);
  }
  .intro__url {
    margin: 4px 0 0;
    font-size: 19px;
    font-weight: 700;
    color: var(--white);
  }
  .services {
    position: absolute;
    left: 874px;
    top: 80px;
    margin: 0;
    padding: 0;
    list-style: none;
  }
  .service {
    display: flex;
    align-items: center;
    height: 88px;
    margin-bottom: 14px;
  }
  .service__icon {
    width: 88px;
    height: 88px;
    flex: none;
  }
  .service__label {
    margin-left: 26px;
    font-size: 34px;
    font-weight: 300;
    letter-spacing: 0.2px;
  }
</style>
</head>
<body>
  <div class="cover">
    <div class="cover__photo" role="img" aria-label="Blurred office photo of business people with a smiling consultant in the foreground, under a dark blue tint"></div>

    <div class="brand-bar">
      <span class="green"></span><span class="blue"></span><span class="purple"></span><span class="orange"></span>
    </div>

    <div class="intro">
      <p class="intro__headline">Find out how Pinecrest can provide<br>customized solutions for your IT needs</p>
      <p class="intro__url">www.pinecrestsolutions-example.com</p>
    </div>

    <ul class="services">
      <li class="service">
        <svg class="service__icon" viewBox="0 0 88 88" aria-hidden="true">
          <circle cx="44" cy="44" r="41" fill="none" stroke="#fff" stroke-width="2"/>
          <circle cx="44" cy="45" r="20" fill="none" stroke="#fff" stroke-width="4"/>
          <circle cx="44" cy="45" r="11" fill="none" stroke="#fff" stroke-width="4"/>
          <circle cx="44" cy="45" r="3" fill="#fff"/>
          <line x1="45" y1="44" x2="60" y2="29" stroke="#fff" stroke-width="3"/>
          <path d="M58 24 l0 7 l7 0 l5 -5 l-6 0 l0 -6 z" fill="#fff"/>
        </svg>
        <span class="service__label">Technology</span>
      </li>
      <li class="service">
        <svg class="service__icon" viewBox="0 0 88 88" aria-hidden="true">
          <circle cx="44" cy="44" r="41" fill="none" stroke="#fff" stroke-width="2"/>
          <rect x="38" y="44" width="22" height="14" fill="none" stroke="#fff" stroke-width="2.5"/>
          <path d="M34 60 h30 l-3 3 h-24 z" fill="#fff"/>
          <g fill="none" stroke="#fff" stroke-width="2.5">
            <circle cx="50" cy="30" r="5"/>
            <circle cx="31" cy="45" r="4"/>
          </g>
          <g stroke="#fff" stroke-width="3">
            <line x1="50" y1="21" x2="50" y2="24"/><line x1="50" y1="36" x2="50" y2="39"/>
            <line x1="41" y1="30" x2="44" y2="30"/><line x1="56" y1="30" x2="59" y2="30"/>
            <line x1="31" y1="38" x2="31" y2="40"/><line x1="31" y1="50" x2="31" y2="52"/>
            <line x1="24" y1="45" x2="26" y2="45"/><line x1="36" y1="45" x2="38" y2="45"/>
          </g>
        </svg>
        <span class="service__label">IT Staffing</span>
      </li>
      <li class="service">
        <svg class="service__icon" viewBox="0 0 88 88" aria-hidden="true">
          <circle cx="44" cy="44" r="41" fill="none" stroke="#fff" stroke-width="2"/>
          <circle cx="44" cy="44" r="22" fill="none" stroke="#fff" stroke-width="3"/>
          <ellipse cx="44" cy="44" rx="10" ry="22" fill="none" stroke="#fff" stroke-width="2"/>
          <line x1="24" y1="34" x2="64" y2="34" stroke="#fff" stroke-width="2"/>
          <line x1="24" y1="54" x2="64" y2="54" stroke="#fff" stroke-width="2"/>
          <rect x="20" y="38" width="48" height="12" fill="#fff"/>
          <text x="44" y="48" text-anchor="middle" font-family="Open Sans, Arial, sans-serif" font-size="10" font-weight="700" fill="#3e4a63">www</text>
        </svg>
        <span class="service__label">IT Domains</span>
      </li>
    </ul>
  </div>
</body>
</html>
```